Lumen Vale Consulting business card

I have a new logo that was designed for me here on CraftHive. I am a medical device marketing consultant. The medical device industry is very professional, kind of dry, and can be a bit boring. But I'm in marketing so I want to look fresh and innovative, within the confines of the industry.

Please use the logo to its potential, making it colorful and visually interesting (I know, there's really only one color. I need some kind of interesting design element - maybe wraparound...

Target Market(s)

Marketing management in medical device companies.

Industry/Entity Type

Marketing

Requirements
Must have
• Melissa Corbin
Phone: 949-555-0143
Address: Dana Point, CA
melissa@lumenvaleconsulting.example
www.lumenvaleconsulting.example

```html
<!DOCTYPE html>
<html lang="en">
<head>
<meta charset="utf-8">
<title>Lumen Vale Consulting – Business Card</title>
<link rel="stylesheet" href="https://fonts.googleapis.com/css2?family=Open+Sans:wght@600&display=swap">
<style>
  :root {
    --page-bg: #e9e6e1;
    --card-black: #1c1c1c;
    --card-black-deep: #111111;
    --card-white: #ffffff;
    --brand-blue: #5b9bd5;
    --band-blue: #243a8c;
    --band-blue-light: #4f6fd0;
    --strip-grey: #2b2b2b;
    --shadow: rgba(0, 0, 0, 0.28);
  }
  * { box-sizing: border-box; margin: 0; padding: 0; }
  html, body {
    width: 1200px;
    height: 750px;
    overflow: hidden;
    background: var(--page-bg);
    font-family: "Open Sans", Arial, sans-serif;
  }
  .canvas {
    position: relative;
    width: 1200px;
    height: 750px;
  }
  .card {
    position: absolute;
    width: 520px;
    height: 297px;
    overflow: hidden;
    box-shadow: 0 6px 18px var(--shadow);
  }

  /* Front of card */
  .card--front {
    left: 70px;
    top: 90px;
    background: radial-gradient(ellipse at 40% 40%, var(--card-black) 0%, var(--card-black-deep) 100%);
  }
  .brand {
    position: absolute;
    left: 70px;
    top: 70px;
    color: var(--brand-blue);
    font-weight: 600;
    line-height: 1;
  }
  .brand__name {
    display: block;
    font-size: 44px;
    letter-spacing: -0.5px;
    white-space: nowrap;
  }
  .brand__descriptor {
    display: block;
    margin-top: 6px;
    margin-left: 96px;
    font-size: 13px;
    letter-spacing: 6px;
  }
  .band {
    position: absolute;
    left: 0;
    top: 196px;
    width: 100%;
    height: 34px;
  }

  /* Back of card */
  .card--back {
    left: 610px;
    top: 380px;
    background: var(--card-black);
  }
  .split {
    position: absolute;
    inset: 0;
    width: 100%;
    height: 100%;
  }
  .feature-name {
    position: absolute;
    left: 22px;
    top: 150px;
    color: var(--brand-blue);
    font-weight: 600;
    font-size: 46px;
    line-height: 1.05;
    letter-spacing: -0.5px;
  }
  .back-strip {
    position: absolute;
    right: 0;
    top: 188px;
    width: 250px;
    height: 60px;
    background: linear-gradient(90deg, var(--strip-grey), rgba(60, 60, 60, 0.85));
    display: flex;
    align-items: center;
    justify-content: center;
  }
  .brand--small {
    position: static;
    text-align: center;
  }
  .brand--small .brand__name {
    font-size: 22px;
  }
  .brand--small .brand__descriptor {
    margin: 3px 0 0;
    font-size: 8px;
    letter-spacing: 3px;
  }
</style>
</head>
<body>
<main class="canvas">

  <section class="card card--front" aria-label="Business card front">
    <div class="brand">
      <span class="brand__name">Lumen Vale</span>
      <span class="brand__descriptor">CONSULTING</span>
    </div>
    <svg class="band" viewBox="0 0 520 34" preserveAspectRatio="none" aria-hidden="true">
      <defs>
        <linearGradient id="band-fill" x1="0" y1="0" x2="1" y2="0">
          <stop offset="0" stop-color="#243a8c"/>
          <stop offset="0.45" stop-color="#4f6fd0"/>
          <stop offset="1" stop-color="#243a8c"/>
        </linearGradient>
        <linearGradient id="spectrum" x1="0" y1="0" x2="1" y2="0">
          <stop offset="0" stop-color="#3aa7e0"/>
          <stop offset="0.3" stop-color="#d0308c"/>
          <stop offset="0.55" stop-color="#e04040"/>
          <stop offset="0.8" stop-color="#e8c030"/>
          <stop offset="1" stop-color="#4cc060"/>
        </linearGradient>
      </defs>
      <rect x="0" y="0" width="520" height="34" fill="url(#band-fill)"/>
      <rect x="0" y="0" width="520" height="1.5" fill="url(#spectrum)"/>
      <rect x="0" y="32.5" width="520" height="1.5" fill="url(#spectrum)"/>
    </svg>
  </section>

  <section class="card card--back" aria-label="Business card back">
    <svg class="split" viewBox="0 0 520 297" preserveAspectRatio="none" aria-hidden="true">
      <polygon points="0,0 232,0 150,297 0,297" fill="#ffffff"/>
      <polygon points="232,0 258,0 176,297 150,297" fill="#5b9bd5"/>
    </svg>
    <div class="feature-name">Lumen<br>Vale</div>
    <div class="back-strip">
      <div class="brand brand--small">
        <span class="brand__name">Lumen Vale</span>
        <span class="brand__descriptor">CONSULTING</span>
      </div>
    </div>
  </section>

</main>
</body>
</html>
```